New Dental Office Needs an Attractive and user friendly Website Designed

I need a website for a new dental office. The Name is Maplecrest Dentistry. I would like a Modern design with a user friendly interface and usability.
I would like a landing page, a page that lists the services we offer: Cosmetic Dentistry, Implants, Dental Hygiene, Emergency Services, Restorations, Dentures
Target Market(s)
Mid to upper class
Industry/Entity Type
Dentistry
Coding
Coded - Design and coding required
Number of Pages Required
1 page
Requirements
Must have
- Landing page that has a scheduling option, Procedures, operating hours, and contact us info
Nice to have
- Appealing design, Soft comforting colors. Easy to navigate page, Modern and professional.

```html
<!DOCTYPE html>
<html lang="en">
<head>
<meta charset="UTF-8">
<title>Maplecrest Dentistry</title>
<link href="https://fonts.googleapis.com/css2?family=Poppins:wght@400;500;600;700&family=Lato:wght@400;700&display=swap" rel="stylesheet">
<style>
:root{
  --ink:#1d1d1f;
  --muted:#6f7378;
  --accent:#3d8be0;
  --accent-soft:#e3edf9;
  --teal:#22bfa2;
  --sky:#19a9e3;
  --sky-deep:#0f9bd8;
  --paper:#ffffff;
  --mist:#f3f4f6;
  --line:#d9dce1;
  --night:#242424;
  --night-text:#d8d8d8;
  --card-tint:#e9f1fb;
  --star:#f4b40b;
}
*{box-sizing:border-box;margin:0;padding:0}
html,body{width:1200px;height:3011px;overflow:hidden}
body{background:var(--paper);color:var(--ink);font-family:'Lato',sans-serif;position:relative}
a{color:inherit;text-decoration:none}

/* hero */
.hero{position:absolute;left:0;top:0;width:1200px;height:602px}
.hero-photo{position:absolute;left:680px;top:0;width:520px;height:549px;background:linear-gradient(160deg,#2cb8ec 0%,var(--sky) 55%,var(--sky-deep) 100%);border-bottom-left-radius:150px;z-index:0}
.nav{position:absolute;z-index:2;left:140px;top:9px;width:919px;height:73px;background:var(--paper);border-radius:6px;box-shadow:0 4px 18px rgba(0,0,0,.08);display:flex;align-items:center;padding:0 25px 0 17px}
.brand{font-family:'Poppins',sans-serif;font-weight:600;font-size:22px;color:var(--ink);display:flex;align-items:center;gap:10px}
.brand-dot{width:14px;height:14px;border-radius:50%;background:var(--teal)}
.nav-links{display:flex;gap:37px;margin-left:auto;margin-right:30px;font-family:'Poppins',sans-serif;font-size:14px}
.btn{display:inline-flex;align-items:center;justify-content:center;font-family:'Poppins',sans-serif;font-size:14px;color:#fff;background:var(--teal);border-radius:3px}
.nav .btn{width:174px;height:32px}
.hero-copy{position:absolute;z-index:1;left:141px;top:170px;width:520px}
.hero-copy h1{font-family:'Poppins',sans-serif;font-weight:400;font-size:46px;line-height:56px;letter-spacing:-.3px}
.hero-copy h1 strong{display:block;font-weight:700;font-size:46px;line-height:56px;letter-spacing:-.5px}
.hero-copy p{font-family:'Poppins',sans-serif;font-size:13.5px;margin-top:14px;white-space:nowrap}
.hero-copy .btn{width:174px;height:33px;margin-top:20px}

/* services */
.services{position:absolute;left:0;top:602px;width:1200px;height:590px;background:var(--mist)}
.sec-title{font-family:'Poppins',sans-serif;font-weight:600;font-size:29px;text-align:center;line-height:36px}
.sec-title span{color:var(--accent)}
.sec-sub{font-size:13px;color:var(--muted);text-align:center;line-height:16px;width:400px;margin:0 auto}
.services .sec-title{margin-top:24px}
.services .sec-sub{margin-top:6px}
.svc-grid{position:absolute;left:140px;top:136px;width:920px;display:grid;grid-template-columns:repeat(3,294px);column-gap:19px;row-gap:36px}
.svc-card{height:175px;background:var(--paper);border:1px solid var(--line);border-radius:14px;text-align:center;padding:24px 22px 0}
.svc-card.active{border:2px solid var(--accent)}
.svc-icon{width:42px;height:42px;border-radius:50%;background:var(--accent-soft);margin:0 auto;display:flex;align-items:center;justify-content:center}
.svc-card.active .svc-icon{background:var(--accent)}
.svc-card h3{font-family:'Poppins',sans-serif;font-weight:600;font-size:19px;margin-top:11px}
.svc-card.active h3{color:var(--accent);font-weight:500}
.svc-card p{font-size:13px;color:var(--muted);line-height:16px;margin-top:2px}
.svc-card.active p{color:var(--ink)}

/* why */
.why{position:absolute;left:0;top:1192px;width:1200px;height:402px;background:var(--night);color:#fff}
.why-intro{position:absolute;left:141px;top:72px;width:270px}
.why-intro h2{font-family:'Poppins',sans-serif;font-weight:600;font-size:28px;line-height:37px}
.why-intro h2 span{color:var(--accent)}
.why-intro p{font-size:13px;line-height:16px;color:var(--night-text);margin-top:10px}
.feat{position:absolute;width:300px}
.feat-head{display:flex;align-items:center;gap:14px}
.feat-icon{width:36px;height:36px;border-radius:50%;background:var(--accent-soft);display:flex;align-items:center;justify-content:center;flex:none}
.feat h3{font-family:'Poppins',sans-serif;font-weight:500;font-size:18.5px;white-space:nowrap}
.feat p{font-size:13px;line-height:16px;color:var(--night-text);margin-top:8px;width:285px}
.feat a{display:inline-block;font-size:13px;text-decoration:underline;margin-top:12px}

/* visit + reviews */
.visit{position:absolute;left:0;top:1594px;width:1200px;height:1175px}
.visit .sec-title{position:absolute;left:0;right:0;top:70px}
.visit .sec-sub.s1{position:absolute;left:0;right:0;top:116px}
.map{position:absolute;left:140px;top:186px;width:643px;height:461px;background:linear-gradient(135deg,#a9cdf2 0%,#dfe6ea 38%,#ece7dc 62%,#a9cdf2 100%)}
.info{position:absolute;left:758px;top:256px;width:301px;height:322px;background:var(--night);border-radius:12px;color:#fff;padding:30px 28px}
.info h4{font-family:'Poppins',sans-serif;font-weight:500;font-size:20px;display:flex;align-items:center;gap:6px}
.info p{font-size:13px;line-height:16px;margin-top:4px}
.info .blk{margin-bottom:18px}
.info .call{display:inline-flex;align-items:center;justify-content:center;width:94px;height:31px;border-radius:16px;background:#fff;color:var(--ink);font-size:13px;font-family:'Poppins',sans-serif;margin-top:-2px}
.visit .rev-title{position:absolute;left:0;right:0;top:718px}
.visit .sec-sub.s2{position:absolute;left:0;right:0;top:768px;width:420px}
.rev{position:absolute;top:839px;width:448px;height:190px;background:var(--card-tint);border-radius:14px;padding:22px 22px}
.rev-top{display:flex;justify-content:space-between;align-items:center}
.stars{display:flex;gap:6px}
.date{font-size:13px}
.rev blockquote{font-size:13px;line-height:16px;margin-top:24px}
.who{display:flex;align-items:center;gap:14px;margin-top:16px}
.avatar{width:56px;height:56px;border-radius:50%;background:linear-gradient(135deg,#c9a27e,#6f5443)}
.who strong{display:block;font-family:'Poppins',sans-serif;font-weight:500;font-size:19px}
.who span{font-size:13px;color:var(--muted)}
.arrow{position:absolute;top:925px;width:29px;height:28px;border-radius:5px;display:flex;align-items:center;justify-content:center}
.arrow.prev{left:91px;border:1.5px solid var(--ink)}
.arrow.next{left:1080px;background:var(--ink)}
.view-all{position:absolute;left:547px;top:1080px;width:105px;height:38px;border-radius:19px;background:var(--accent);color:#fff;font-family:'Poppins',sans-serif;font-size:13px;display:flex;align-items:center;justify-content:center}

/* footer */
.footer{position:absolute;left:0;top:2769px;width:1200px;height:242px;background:var(--night);color:#fff}
.footer .brand{color:#fff;position:absolute;left:0;right:0;top:60px;justify-content:center;font-size:22px}
.foot-links{position:absolute;left:0;right:0;top:125px;display:flex;justify-content:center;gap:29px;font-family:'Poppins',sans-serif;font-size:13px}
.foot-rule{position:absolute;left:0;right:0;top:199px;height:1px;background:#3a3a3a}
.copy{position:absolute;left:0;right:0;top:213px;text-align:center;font-size:11px;color:var(--night-text)}
</style>
</head>
<body>

<header class="hero">
  <div class="hero-photo" role="img" aria-label="Smiling young man in a denim shirt against a bright blue backdrop"></div>
  <nav class="nav">
    <a class="brand" href="#"><span class="brand-dot"></span>Maplecrest Dentistry</a>
    <div class="nav-links"><a href="#">Home</a><a href="#">About</a><a href="#">Services</a><a href="#">Contact</a></div>
    <a class="btn" href="#">Book an Appointment</a>
  </nav>
  <div class="hero-copy">
    <h1>Smile Confidently.<strong>Feel the Difference.</strong></h1>
    <p>Premium Dental Care Tailored to You – Where Comfort Meets Excellence</p>
    <a class="btn" href="#">Book an Appointment</a>
  </div>
</header>

<section class="services">
  <h2 class="sec-title">Our Dental <span>Services</span></h2>
  <p class="sec-sub">Comprehensive, high-quality care from cosmetic enhancements to emergency treatments—tailored to your smile.</p>
  <div class="svc-grid">
    <article class="svc-card">
      <div class="svc-icon"><svg width="24" height="24" viewBox="0 0 24 24" fill="none" stroke="#3d8be0" stroke-width="1.5"><circle cx="12" cy="12" r="9"/><path d="M8 14c1.2 1.6 2.4 2.2 4 2.2s2.8-.6 4-2.2"/><circle cx="9" cy="10" r=".8" fill="#3d8be0"/><circle cx="15" cy="10" r=".8" fill="#3d8be0"/></svg></div>
      <h3>Cosmetic Dentistry</h3>
      <p>Enhance your smile with treatments that improve tooth shape, color, and appearance.</p>
    </article>
    <article class="svc-card active">
      <div class="svc-icon"><svg width="24" height="24" viewBox="0 0 24 24" fill="none" stroke="#fff" stroke-width="1.6"><path d="M7 4c2-1 3 0 5 0s3-1 5 0c2 1 1.5 5 0 7H7C5.5 9 5 5 7 4z"/><path d="M9 13h6M9.5 16h5M10.5 19h3"/></svg></div>
      <h3>Dental Implants</h3>
      <p>Permanent, natural-looking tooth replacements that restore function and confidence.</p>
    </article>
    <article class="svc-card">
      <div class="svc-icon"><svg width="24" height="24" viewBox="0 0 24 24" fill="none" stroke="#3d8be0" stroke-width="1.5"><path d="M5 5l14 14M19 5L5 19"/><rect x="3" y="3" width="5" height="5" rx="1"/><rect x="16" y="16" width="5" height="5" rx="1"/></svg></div>
      <h3>Emergency Services</h3>
      <p>Quick, professional treatment for dental emergencies, providing relief when you need it most.</p>
    </article>
    <article class="svc-card">
      <div class="svc-icon"><svg width="24" height="24" viewBox="0 0 24 24" fill="none" stroke="#3d8be0" stroke-width="1.5"><path d="M3 9c3 6 15 6 18 0"/><path d="M5 10.5l1 3M9 12l.5 2.5M12 12.3V15M15 12l-.5 2.5M19 10.5l-1 3"/></svg></div>
      <h3>Teeth Whitening</h3>
      <p>Brighten your smile with safe, professional whitening treatments that deliver fast, noticeable results.</p>
    </article>
    <article class="svc-card">
      <div class="svc-icon"><svg width="24" height="24" viewBox="0 0 24 24" fill="none" stroke="#3d8be0" stroke-width="1.5"><path d="M7 3.5c2-1 3 .2 5 .2s3-1.2 5-.2c2.5 1.3 2 6-.5 9.5l-1 7c-.3 1-1.5 1-1.8 0L12 15l-1.7 5c-.3 1-1.5 1-1.8 0l-1-7C5 9.5 4.5 4.8 7 3.5z"/></svg></div>
      <h3>Dental Hygiene</h3>
      <p>Preventive cleanings and exams to keep your teeth and gums healthy, fresh, and cavity-free.</p>
    </article>
    <article class="svc-card">
      <div class="svc-icon"><svg width="24" height="24" viewBox="0 0 24 24" fill="none" stroke="#3d8be0" stroke-width="1.5"><path d="M7 3.5c2-1 3 .2 5 .2s3-1.2 5-.2c2.5 1.3 2 6-.5 9.5l-1 7c-.3 1-1.5 1-1.8 0L12 15l-1.7 5c-.3 1-1.5 1-1.8 0l-1-7C5 9.5 4.5 4.8 7 3.5z"/><path d="M9 7c1 .6 2 .6 3 0"/></svg></div>
      <h3>Tooth Restoration</h3>
      <p>Repair and restore damaged teeth with natural-looking fillings, crowns, and bridges for a healthier smile.</p>
    </article>
  </div>
</section>

<section class="why">
  <div class="why-intro">
    <h2>Why Patients Choose <span>Our Clinic</span></h2>
    <p>Experience expert care in a modern, comfort-first clinic—where advanced technology meets personalized treatment.</p>
  </div>
  <div class="feat" style="left:443px;top:71px">
    <div class="feat-head"><span class="feat-icon"><svg width="18" height="18" viewBox="0 0 24 24" fill="none" stroke="#3d8be0" stroke-width="2"><rect x="4" y="6" width="16" height="12" rx="2"/><circle cx="12" cy="12" r="2.5"/></svg></span><h3>Board-Certified Dentists</h3></div>
    <p>Expertise you can trust, backed by advanced training and credentials.</p>
    <a href="#">Learn more</a>
  </div>
  <div class="feat" style="left:765px;top:71px">
    <div class="feat-head"><span class="feat-icon"><svg width="18" height="18" viewBox="0 0 24 24" fill="none" stroke="#3d8be0" stroke-width="2"><path d="M7 4c2-1 3 0 5 0s3-1 5 0c2 1 1.5 5 0 8l-1 7c-.3 1-1.5 1-1.8 0L12 15l-2.2 4c-.3 1-1.5 1-1.8 0l-1-7C5.5 9 5 5 7 4z"/></svg></span><h3>Pain-Free Treatments</h3></div>
    <p>Gentle techniques and modern technology for a stress-free experience.</p>
    <a href="#">Learn more</a>
  </div>
  <div class="feat" style="left:443px;top:229px">
    <div class="feat-head"><span class="feat-icon"><svg width="18" height="18" viewBox="0 0 24 24" fill="none" stroke="#3d8be0" stroke-width="2"><path d="M5 5c0 6 4 10 10 10h4v3H8"/><path d="M12 8l4 4"/></svg></span><h3>Luxury, Comfort Clinic</h3></div>
    <p>Designed to help you relax—because your comfort matters.</p>
    <a href="#">Learn more</a>
  </div>
  <div class="feat" style="left:765px;top:229px">
    <div class="feat-head"><span class="feat-icon"><svg width="18" height="18" viewBox="0 0 24 24" fill="#3d8be0"><rect x="3" y="7" width="18" height="12" rx="2"/><rect x="6" y="4" width="10" height="4" rx="1"/></svg></span><h3>Flexible Payment Plans</h3></div>
    <p>Quality care made accessible with tailored financing options.</p>
    <a href="#">Learn more</a>
  </div>
</section>

<section class="visit">
  <h2 class="sec-title">Visit Our <span>Clinic</span></h2>
  <p class="sec-sub s1">Located in the heart of Crestview, our clinic offers flexible hours and easy access to premium dental care.</p>
  <div class="map" role="img" aria-label="Street map showing the clinic location and surrounding neighbourhoods"></div>
  <aside class="info">
    <div class="blk">
      <h4><svg width="18" height="18" viewBox="0 0 24 24" fill="none" stroke="#3d8be0" stroke-width="2"><path d="M12 21s-7-6.5-7-12a7 7 0 0114 0c0 5.5-7 12-7 12z"/><circle cx="12" cy="9" r="2.5"/></svg>Visit Us</h4>
      <p style="padding-left:8px">48 Willow Bend Road, Crestview</p>
    </div>
    <div class="blk">
      <h4><svg width="18" height="18" viewBox="0 0 24 24" fill="none" stroke="#3d8be0" stroke-width="2"><circle cx="12" cy="12" r="9"/><path d="M12 7v5l3 2"/></svg>Operating Hours</h4>
      <p>Mon–Fri: 8:00 AM – 6:00 PM<br>Sat: 9:00 AM – 2:00 PM<br>Closed Sundays</p>
    </div>
    <div class="blk">
      <h4><svg width="18" height="18" viewBox="0 0 24 24" fill="none" stroke="#3d8be0" stroke-width="2"><path d="M5 4h4l2 5-2.5 1.5a11 11 0 005 5L15 13l5 2v4a2 2 0 01-2 2A16 16 0 013 6a2 2 0 012-2z"/></svg>Call Us</h4>
      <p>(555) 218-4630</p>
    </div>
    <a class="call" href="#">Call Now</a>
  </aside>

  <h2 class="sec-title rev-title">What Our <span>Patients Say</span></h2>
  <p class="sec-sub s2">Real stories from patients who've experienced compassionate care, outstanding results, and a confident new smile.</p>

  <a class="arrow prev" href="#" aria-label="Previous"><svg width="12" height="12" viewBox="0 0 12 12" fill="none" stroke="#1d1d1f" stroke-width="1.6"><path d="M8 1L3 6l5 5"/></svg></a>

  <article class="rev" style="left:141px">
    <div class="rev-top">
      <div class="stars">
        <svg width="20" height="19" viewBox="0 0 24 23"><path fill="#f4b40b" d="M12 0l3.5 7.6 8.3.9-6.2 5.6 1.8 8.2L12 18l-7.4 4.3 1.8-8.2L.2 8.5l8.3-.9z"/></svg>
        <svg width="20" height="19" viewBox="0 0 24 23"><path fill="#f4b40b" d="M12 0l3.5 7.6 8.3.9-6.2 5.6 1.8 8.2L12 18l-7.4 4.3 1.8-8.2L.2 8.5l8.3-.9z"/></svg>
        <svg width="20" height="19" viewBox="0 0 24 23"><path fill="#f4b40b" d="M12 0l3.5 7.6 8.3.9-6.2 5.6 1.8 8.2L12 18l-7.4 4.3 1.8-8.2L.2 8.5l8.3-.9z"/></svg>
        <svg width="20" height="19" viewBox="0 0 24 23"><path fill="#f4b40b" d="M12 0l3.5 7.6 8.3.9-6.2 5.6 1.8 8.2L12 18l-7.4 4.3 1.8-8.2L.2 8.5l8.3-.9z"/></svg>
        <svg width="20" height="19" viewBox="0 0 24 23"><path fill="#f4b40b" d="M12 0l3.5 7.6 8.3.9-6.2 5.6 1.8 8.2L12 18l-7.4 4.3 1.8-8.2L.2 8.5l8.3-.9z"/></svg>
      </div>
      <span class="date">10th Feb, 2023</span>
    </div>
    <blockquote>"The team made me feel comfortable from the moment I walked in. My smile has never looked better!"</blockquote>
    <div class="who"><div class="avatar" role="img" aria-label="Portrait of the patient"></div><div><strong>Daniel R.</strong><span>Customer</span></div></div>
  </article>

  <article class="rev" style="left:610px">
    <div class="rev-top">
      <div class="stars">
        <svg width="20" height="19" viewBox="0 0 24 23"><path fill="#f4b40b" d="M12 0l3.5 7.6 8.3.9-6.2 5.6 1.8 8.2L12 18l-7.4 4.3 1.8-8.2L.2 8.5l8.3-.9z"/></svg>
        <svg width="20" height="19" viewBox="0 0 24 23"><path fill="#f4b40b" d="M12 0l3.5 7.6 8.3.9-6.2 5.6 1.8 8.2L12 18l-7.4 4.3 1.8-8.2L.2 8.5l8.3-.9z"/></svg>
        <svg width="20" height="19" viewBox="0 0 24 23"><path fill="#f4b40b" d="M12 0l3.5 7.6 8.3.9-6.2 5.6 1.8 8.2L12 18l-7.4 4.3 1.8-8.2L.2 8.5l8.3-.9z"/></svg>
        <svg width="20" height="19" viewBox="0 0 24 23"><path fill="#f4b40b" d="M12 0l3.5 7.6 8.3.9-6.2 5.6 1.8 8.2L12 18l-7.4 4.3 1.8-8.2L.2 8.5l8.3-.9z"/></svg>
        <svg width="20" height="19" viewBox="0 0 24 23"><path fill="#f4b40b" d="M12 0l3.5 7.6 8.3.9-6.2 5.6 1.8 8.2L12 18l-7.4 4.3 1.8-8.2L.2 8.5l8.3-.9z"/></svg>
      </div>
      <span class="date">06th Feb, 2023</span>
    </div>
    <blockquote>"Beautiful clinic, friendly staff, and pain-free treatment. Truly a premium dental experience."</blockquote>
    <div class="who"><div class="avatar" style="background:linear-gradient(135deg,#f1d27a,#c8955c)" role="img" aria-label="Portrait of the patient"></div><div><strong>Olivia K.</strong><span>Customer</span></div></div>
  </article>

  <a class="arrow next" href="#" aria-label="Next"><svg width="12" height="12" viewBox="0 0 12 12" fill="none" stroke="#fff" stroke-width="1.6"><path d="M4 1l5 5-5 5"/></svg></a>

  <a class="view-all" href="#">View All</a>
</section>

<footer class="footer">
  <a class="brand" href="#"><span class="brand-dot"></span>Maplecrest Dentistry</a>
  <nav class="foot-links"><a href="#">Home</a><a href="#">Our Services</a><a href="#">Contact Us</a></nav>
  <div class="foot-rule"></div>
  <p class="copy">© 2025 Maplecrest Dental Care. All Rights Reserved.</p>
</footer>

</body>
</html>
```